Newsletter-Design für Online-Versandhandel
Zielgruppe
Wir sind ein online Versand Handel mit dem Schwerpunkt auf Bio Bettwaren. Unsere Zielgruppe sind ökologisch bewusste Menschen mittleren bis höheren Alters.
Aufgabenstellung
Unsere Corporate Farbe ist vornehmlich ein sanftes Grün.
www.bettwelt-lindqvar.example
Hier eine Auswahl von Newslettern
http://newsletter.waldmoos-shop.example/u/gm.php?prm=4pTrKmZyyQ_815204736_5390418_23847
http://newslink.lodenfalt.example/u/gm.php?prm=bRx72kdfQ_962157384_3047215_81530
Bisher haben wir unsere NL als kleinen, persönlichen Text gestaltet und dazu zwei oder drei Teaser.
Den Text möchte ich beibehalten und neben meiner Unterschrift ein ein kleines persönliches Bild einfügen.
Wichtig! Wir versenden mit postfink, wir benötigen eine dafür kompatible Vorlage.

```html
<!DOCTYPE html>
<html lang="de">
<head>
<meta charset="utf-8">
<title>Lindqvar Naturversand – Newsletter</title>
<link href="https://fonts.googleapis.com/css2?family=Open+Sans:wght@400;600;700&display=swap" rel="stylesheet">
<style>
:root{
  --green:#0b9447;
  --green-bright:#22b85c;
  --green-dark:#0c7638;
  --text:#333;
  --muted:#8a8a8a;
  --gray-bg:#f4f4f4;
  --cream:#fdf6de;
  --blue:#1b84d6;
}
*{box-sizing:border-box;margin:0;padding:0}
html,body{width:1200px;height:3400px;overflow:hidden;background:#fff;font-family:"Open Sans",sans-serif;color:var(--text)}
.mail{position:absolute;left:179px;top:0;width:842px}
.header{height:113px;position:relative}
.brand{position:absolute;left:22px;top:12px}
.brand-row{display:flex;align-items:center;gap:8px}
.brand-dot{width:40px;height:40px;border-radius:50%;background:var(--green)}
.brand-name{font-size:28px;font-weight:700;color:var(--green)}
.brand-since{font-size:11px;color:var(--green);font-weight:600;margin-left:6px}
.brand-sub{font-size:17px;letter-spacing:2px;color:var(--green-bright);margin-top:4px}
.contact-top{position:absolute;right:40px;top:32px;text-align:right;font-size:13px;line-height:18px}
.contact-top strong{font-weight:700}
.nav{height:45px;background:var(--green);display:flex;align-items:center;padding-left:29px;gap:0}
.nav a{color:#fff;text-decoration:none;font-size:14px;font-weight:600}
.hero{height:290px;background:var(--cream);position:relative;overflow:hidden}
.ph{display:block}
.hero-photo{position:absolute;left:0;top:0;width:277px;height:290px;background:linear-gradient(135deg,#c9a98a,#e8d2b8 60%,#bdb0a0)}
.hero-note{position:absolute;left:180px;top:120px;width:210px;height:170px;background:linear-gradient(120deg,#d7cfc0,#eee5d4)}
.hero-star{position:absolute;left:290px;top:35px}
.hero-copy{position:absolute;left:523px;top:10px;width:310px}
.hero-copy p.lead{font-size:19px;line-height:24px;color:#333}
.hero-copy h2{font-size:29px;line-height:35px;color:var(--blue);font-weight:700;margin-top:12px}
.hero-copy p.small{font-size:12px;line-height:18px;margin-top:10px}
.btn-hero{display:inline-block;margin-top:14px;background:var(--green-bright);color:#fff;font-size:14px;padding:4px 14px;border-radius:3px}
.welcome{text-align:center;padding:56px 30px 0;height:285px}
.welcome h1,.section-title{font-size:23px;font-weight:600;letter-spacing:.3px}
.rule{width:66px;height:2px;background:var(--green);margin:20px auto 18px}
.welcome p{font-size:12px;line-height:20.5px;color:var(--muted)}
.advice{height:184px;background:var(--green);color:#fff;text-align:center;padding-top:34px}
.advice h2{font-size:23px;font-weight:600}
.advice .rule{background:#fff;margin:20px auto 24px}
.advice-row{display:flex;justify-content:center;gap:11px}
.pill{border:1px solid #fff;height:36px;display:flex;align-items:center;gap:10px;padding:0 14px;font-size:14px}
.teasers{display:flex;gap:21px;padding:56px 29px 0;height:404px}
.teaser{width:249px}
.teaser .ph{height:187px}
.teaser h3{font-size:19px;font-weight:400;line-height:25px;margin-top:18px}
.teaser p{font-size:12.5px;line-height:21px;color:var(--muted);margin-top:6px;height:44px}
.btn{display:inline-block;background:var(--green);color:#fff;font-size:11.5px;font-weight:700;padding:8px 12px;margin-top:14px}
.banner{height:224px;position:relative;background:linear-gradient(90deg,#6f6f6f,#9a9a9a 50%,#7a7a7a);color:#fff;text-align:center;padding-top:46px}
.banner h2{font-size:24px;font-weight:600}
.banner p{font-size:17px;line-height:24px;margin-top:4px}
.btn-dark{display:inline-block;background:#2f2f2f;color:#fff;font-size:13px;padding:8px 32px;border-radius:18px;margin-top:14px}
.range{background:var(--gray-bg);height:683px;padding:62px 29px 0;text-align:center}
.range .rule{margin-bottom:48px}
.product{background:#fff;height:222px;position:relative;text-align:left;margin-bottom:30px}
.product .ph{position:absolute;left:20px;top:30px;width:175px;height:165px;border:1px solid #e3e3e3}
.product h3{position:absolute;left:210px;top:30px;font-size:18px;font-weight:400}
.product p{position:absolute;left:211px;top:58px;width:540px;font-size:12px;line-height:17.5px;color:var(--muted)}
.product p span{display:block;margin-top:12px}
.btn-light{position:absolute;right:0;bottom:0;background:var(--green-bright);color:#fff;font-size:11.5px;font-weight:700;padding:8px 15px}
.top{position:relative;height:721px}
.top-bg{position:absolute;left:0;top:0;width:842px;height:327px;background:linear-gradient(180deg,#8a8a8a,#b5b5b5)}
.top h2{position:absolute;left:0;width:842px;top:68px;text-align:center;color:#fff;font-size:24px;font-weight:600}
.top-arrow{position:absolute;left:404px;top:117px}
.card{position:absolute;background:#fff;width:262px;box-shadow:0 1px 4px rgba(0,0,0,.12);padding-bottom:20px}
.card .ph{height:168px}
.card h3{font-size:19px;font-weight:400;margin:22px 0 6px 16px}
.card li{list-style:none;font-size:13px;line-height:25px;color:#555;margin-left:16px}
.card .btn-card{display:block;background:var(--green-bright);color:#fff;text-align:center;font-size:11.5px;font-weight:700;padding:8px 0;margin:12px 22px 0}
.pay{height:85px;background:#efefef;display:flex;align-items:center;gap:40px;padding-left:26px}
.pay .seal{width:56px;height:56px;border-radius:50%;background:#cfcfcf}
.pay .ship{width:232px;height:46px;background:#d4d4d4}
.pay .chip{width:125px;height:30px;background:#d6d6d6;border-radius:4px}
.footer{height:248px;background:var(--green-bright);color:#fff;display:flex;padding:56px 0 0 17px;font-size:13px;line-height:22.5px}
.footer h4{font-size:12.5px;font-weight:700;margin-bottom:1px}
.col1{width:163px}.col2{width:237px}.col3{width:223px}
.legal{height:54px;background:var(--green-dark);color:#fff;font-size:12.5px;text-align:center;padding-top:16px}
</style>
</head>
<body>
<div class="mail">
  <header class="header">
    <div class="brand">
      <div class="brand-row"><span class="brand-dot"></span><span class="brand-name">Lindqvar</span><span class="brand-since">Seit 25 Jahren</span></div>
      <div class="brand-sub">NATURVERSAND-ONLINESHOP</div>
    </div>
    <div class="contact-top"><strong>WIR BERATEN SIE GERNE!</strong><br>Telefonisch unter 04321/55870-20<br>Mo-Do 9-12 und 12-17 Uhr, Fr 10-12 Uhr</div>
  </header>
  <nav class="nav">
    <a href="#" style="margin-right:26px">Home</a><a href="#" style="margin-right:29px">Schlafen</a><a href="#" style="margin-right:47px">Handwebteppiche</a><a href="#" style="margin-right:37px">Edelstein-Schmuck</a><a href="#" style="margin-right:47px">Wärmeauflagen</a><a href="#">Allergikerprodukte</a>
  </nav>
  <section class="hero">
    <div class="ph hero-photo" role="img" aria-label="Foto einer lächelnden Frau"></div>
    <div class="ph hero-note" role="img" aria-label="Geldschein mit Herzanhänger"></div>
    <svg class="hero-star" width="200" height="200" viewBox="0 0 200 200">
      <polygon fill="var(--blue)" points="100,5 114,38 146,18 146,54 184,50 164,82 196,100 164,118 184,150 146,146 146,182 114,162 100,195 86,162 54,182 54,146 16,150 36,118 4,100 36,82 16,50 54,54 54,18 86,38"/>
      <text x="100" y="93" fill="#fff" font-family="Open Sans, sans-serif" font-weight="700" font-size="25" text-anchor="middle">Einfach</text>
      <text x="100" y="122" fill="#fff" font-family="Open Sans, sans-serif" font-weight="700" font-size="25" text-anchor="middle">geschenkt!</text>
    </svg>
    <div class="hero-copy">
      <p class="lead">Melden Sie sich jetzt für unseren Newsletter an und erhalten Sie</p>
      <h2>20,- EURO RABATT EINFACH GESCHENKT</h2>
      <p class="small">Verpassen Sie nie wieder Spezial-Angebote, Rabatt-Aktionen, Neuigkeiten und Tipps rund um's natürliche Wohnen und gesunde Schlafen.</p>
      <span class="btn-hero">Weitere Informationen</span>
    </div>
  </section>
  <section class="welcome">
    <h1>HERZLICH WILLKOMMEN BEI LINDQVAR NATURVERSAND!</h1>
    <div class="rule"></div>
    <p>Kaufen Sie bei uns hochwertige, ökologische Produkte für natürliches Wohnen und gesundes Schlafen. Bei uns finden Sie Oberbetten, Handwebteppiche, Produkte zum Schutz vor Elektrosmog, orthopädische Kissen, Allergiker Bettdecken, Kirschkernkissen, Nackenwärmer, Daunenkissen, Kaschmirdecken. Liegen Sie gesund und richtig in unseren Massivholzbetten, auf unseren Naturlatexmatratzen und unseren Bio Lattenrosten. Kuscheln Sie sich in unsere ökologischen Bettwaren aus kbA Baumwolle mit den verschiedensten Füllungen.</p>
  </section>
  <section class="advice">
    <h2>WIR BERATEN SIE GERN!</h2>
    <div class="rule"></div>
    <div class="advice-row">
      <div class="pill"><svg width="20" height="20" viewBox="0 0 24 24" fill="none" stroke="#fff" stroke-width="1.6"><path d="M5 3h4l2 5-3 2a12 12 0 0 0 6 6l2-3 5 2v4a2 2 0 0 1-2 2A17 17 0 0 1 3 5a2 2 0 0 1 2-2z"/></svg>TELEFONISCH UNTER 04321 / 55870-20</div>
      <div class="pill"><svg width="20" height="20" viewBox="0 0 24 24" fill="none" stroke="#fff" stroke-width="1.6"><rect x="3" y="5" width="18" height="16" rx="1"/><path d="M3 10h18M8 3v4M16 3v4"/></svg>MO-DO 9-12 UND 12-17 UHR, FR 10-12 UHR</div>
    </div>
  </section>
  <section class="teasers">
    <article class="teaser"><div class="ph" role="img" aria-label="Schlafende Frau im Bett" style="background:linear-gradient(135deg,#d9cfc4,#f2ece6)"></div><h3>Hochwertige Bettdecken aus Schafschurwolle</h3><p>besonders haut- und klimafre undlich</p><span class="btn">WEITERLESEN</span></article>
    <article class="teaser"><div class="ph" role="img" aria-label="Hände massieren einen Nacken" style="background:linear-gradient(135deg,#d8b49e,#eed8c8)"></div><h3>Warmeauflagen gegen Nackenverspannungen</h3><p>von Hand gefertigt,speziell fur Sie abgestimmt.</p><span class="btn">WEITERLESEN</span></article>
    <article class="teaser"><div class="ph" role="img" aria-label="Frau mit Taschentuch auf einer Wiese" style="background:linear-gradient(135deg,#a9b56a,#d7d8a4)"></div><h3>Biologische Allergikerproduckte</h3><p>Lindern Beschweden bei Hausstauballergie</p><span class="btn">WEITERLESEN</span></article>
  </section>
  <section class="banner" role="img" aria-label="Frau mit Kissen im Schlafzimmer als Hintergrund">
    <h2>WELCHES BETT IST FÜR MICH DAS RICHTIGE?</h2>
    <p>Unser Ratgeber hilft Ihnen, das optimale Material für Ihre<br>Bettdecke und Ihr Kissen zu finden.</p>
    <span class="btn-dark">WEITERLESEN</span>
  </section>
  <section class="range">
    <h2 class="section-title">FÜR BETTWAREN, TEPPICHE UND ALLERGIEPRODUKTE</h2>
    <div class="rule"></div>
    <article class="product">
      <div class="ph" role="img" aria-label="Gestreifter Handwebteppich" style="background:linear-gradient(160deg,#e9e4dc,#c24a3a 55%,#2f4e86)"></div>
      <h3>Handwebteppiche</h3>
      <p>Gerade in Zeiten des schnellen Wandels und der Massenware ist es wichtig wie nie, an bestimmten Werten festzuhalten und diese weiterzugeben: Tradition, Nachhaltigkeit, Qualität und Individualität. Doch diese Werte sollten wir nicht nur in unserem alltäglichen Handeln schützen, sondern auch in unserer Umgebung.<span>Mit einem handgewebten Teppich aus dem Allgäu kommen Sie diesem Wunsch ein Stückchen näher.</span></p>
      <span class="btn-light">ÜBERPRÜFEN SIE DIE PRODUKTE</span>
    </article>
    <article class="product">
      <div class="ph" role="img" aria-label="Kind mit Taschentuch" style="background:linear-gradient(160deg,#e2b07a,#7fb8d8)"></div>
      <h3>Allergikerprodukte</h3>
      <p>Hausstaubmilben leben im Schlafzimmer vor allem in textilen Gegenständen - in Matratzen, Kissen, Bettdecken und Textilien.<span style="margin-top:18px">Bettdecken, Kissen und Bettwäsche müssen mindestens alle 4-6 Wochen bei 60°C gewaschen werden. Milben sterben erst bei einer Temperatur von 60°C</span></p>
      <span class="btn-light">ÜBERPRÜFEN SIE DIE PRODUKTE</span>
    </article>
  </section>
  <section class="top">
    <div class="top-bg" role="img" aria-label="Frau schüttelt Bettdecke im hellen Schlafzimmer"></div>
    <h2>Schauen Sie sich unsere weiteren Top-Produkte an</h2>
    <svg class="top-arrow" width="34" height="34" viewBox="0 0 34 34"><circle cx="17" cy="17" r="17" fill="var(--green-bright)"/><path d="M11 11l6 6 6-6M11 17l6 6 6-6" fill="none" stroke="#fff" stroke-width="2"/></svg>
    <div class="card" style="left:17px;top:222px">
      <div class="ph" role="img" aria-label="Holzbett im Schlafzimmer" style="background:linear-gradient(135deg,#e7e3dc,#c9ad88)"></div>
      <h3>Schlafen</h3>
      <ul><li>Bettdecken</li><li>Kopfkissen</li><li>Bettwäsche</li><li>Matratzen und Lattenroste</li></ul>
      <span class="btn-card">SIEHE PRODUKTE</span>
    </div>
    <div class="card" style="left:291px;top:175px">
      <div class="ph" role="img" aria-label="Frau mit Wärmeauflage auf dem Rücken" style="background:linear-gradient(135deg,#4a4f5a,#e9dcc4)"></div>
      <h3>Wärmeauflagen</h3>
      <ul><li>Wärmeauflagen Sets</li><li>Intensive Wärmetherapie</li><li>Sanfte Wärmetherapie</li><li>Kopfschmerzen</li><li>Schlafbrille</li><li>Heilmoor-Produkte</li></ul>
      <span class="btn-card">SIEHE PRODUKTE</span>
    </div>
    <div class="card" style="left:566px;top:222px">
      <div class="ph" role="img" aria-label="Frau zeigt Ringe mit Edelsteinen" style="background:linear-gradient(135deg,#6b4a3a,#d9b59a)"></div>
      <h3>Edelstein-Schmuck</h3>
      <ul><li>Halsketten</li><li>Amethyst</li><li>Bergkristall</li><li>Armbänder</li></ul>
      <span class="btn-card">SIEHE PRODUKTE</span>
    </div>
  </section>
  <section class="pay">
    <span class="seal" role="img" aria-label="Gütesiegel"></span>
    <span class="ship" role="img" aria-label="Versandpartner"></span>
    <span class="chip" role="img" aria-label="Zahlungsart"></span>
    <span class="chip" role="img" aria-label="Zahlungsart" style="width:120px"></span>
    <span class="chip" role="img" aria-label="Zahlung auf Rechnung" style="width:120px"></span>
  </section>
  <footer class="footer">
    <div class="col1"><h4>SERVICE</h4>Bettdecken-Ratgeber<br>Kissen-Ratgeber<br>Newsletter-Anmeldung<br>Rückruf-Service</div>
    <div class="col2"><h4>INFORMATIONEN</h4>Allgemeine Geschäftsbedingungen<br>Datenschutzerklärung<br>Impressum<br>Versand<br>Widerrufsrecht<br>Zahlungsmöglichkeiten</div>
    <div class="col3"><h4>ÜBER UNS</h4>Firmenhistorie<br>Eigene Manufaktur<br>Natürliche Materialien<br>Unser Beitrag zum Umweltschutz</div>
    <div><h4>KONTAKT</h4>Telefonisch unter:<br>04321 558 7021<br>per E-Mail unter<br>info@bettwelt-lindqvar.example</div>
  </footer>
  <div class="legal">* Alle Preise inkl. gesetzl. Mehrwertsteuer und zzgl. der Versandkosten. Innerhalb Deutschlands versenden wir portofrei.</div>
</div>
</body>
</html>
```